FC Morlan - Creation of a AD banner for our yearly event

We are a local soccer club in Switzerland. We're organizing a event that will substitute to our yearly club dinner. We need a banner AD to promote on the social networks this event.
We would like to see design that use one or the 2 colors of the club (blue and red).
This Ad should link to a online shop where we can buy vouchers.

Requirements
Must have
• Logo of the club
Title : Fête des lanternes d'hiver
Call to action : Plus d'informations
Side texte : Grande Tombola
Banner size : W300xH250 or W300xH600
Nice to have
• Promotion texte: Soutenez le FC Morlan et les restaurateurs locaux

```html
<!DOCTYPE html>
<html lang="fr">
<head>
<meta charset="utf-8">
<title>FC Morlan – Fête des lanternes d'hiver</title>
<link rel="stylesheet" href="https://fonts.googleapis.com/css2?family=Saira+Condensed:wght@700;800;900&family=Teko:wght@500;600&family=Open+Sans:wght@400;600&display=swap">
<style>
  :root {
    --grass-light: #4fae3a;
    --grass-mid: #2f8a24;
    --grass-dark: #15520f;
    --silver-top: #ffffff;
    --silver-mid: #c9cdd2;
    --silver-low: #8d939a;
    --silver-edge: #f2f4f6;
    --club-white: #ffffff;
    --club-red: #e8344a;
    --cta-bg: #000000;
    --cta-text: #ffffff;
  }
  * { margin: 0; padding: 0; box-sizing: border-box; }
  html, body { width: 1200px; height: 1000px; overflow: hidden; background: var(--grass-dark); }

  .banner {
    position: relative;
    width: 1200px;
    height: 1000px;
    overflow: hidden;
  }

  .banner__turf {
    position: absolute;
    inset: 0;
    background:
      radial-gradient(ellipse 60% 50% at 50% 45%, var(--grass-light) 0%, rgba(79,174,58,0) 70%),
      radial-gradient(ellipse 120% 100% at 50% 50%, var(--grass-mid) 30%, var(--grass-dark) 100%);
  }

  .club-mark {
    position: absolute;
    left: 36px;
    top: 40px;
    display: flex;
    align-items: center;
    gap: 12px;
  }
  .club-mark__square {
    width: 26px;
    height: 26px;
    background: var(--club-red);
  }
  .club-mark__name {
    font-family: "Saira Condensed", sans-serif;
    font-weight: 800;
    font-size: 34px;
    color: var(--club-white);
    letter-spacing: 1px;
  }

  .silver {
    background: linear-gradient(180deg, var(--silver-top) 0%, var(--silver-mid) 45%, var(--silver-low) 55%, var(--silver-edge) 100%);
    -webkit-background-clip: text;
    background-clip: text;
    color: transparent;
    filter: drop-shadow(0 4px 4px rgba(0,0,0,0.55));
  }

  .kicker {
    position: absolute;
    top: 104px;
    left: 0;
    width: 100%;
    text-align: center;
    font-family: "Teko", sans-serif;
    font-weight: 600;
    font-size: 92px;
    line-height: 1;
    letter-spacing: 6px;
  }

  .headline {
    position: absolute;
    top: 290px;
    left: 0;
    width: 100%;
    text-align: center;
    font-family: "Saira Condensed", sans-serif;
    font-weight: 900;
    font-style: italic;
    text-transform: uppercase;
    line-height: 0.98;
    transform: skewX(-8deg);
  }
  .headline__line { display: block; }
  .headline__line--first { font-size: 142px; letter-spacing: 2px; }
  .headline__line--second { font-size: 172px; letter-spacing: 6px; }

  .cta {
    position: absolute;
    left: 318px;
    top: 780px;
    width: 568px;
    height: 106px;
    background: var(--cta-bg);
    color: var(--cta-text);
    display: flex;
    align-items: center;
    justify-content: center;
    font-family: "Open Sans", sans-serif;
    font-weight: 400;
    font-size: 47px;
    text-decoration: none;
  }

  .tagline {
    position: absolute;
    top: 912px;
    left: 0;
    width: 100%;
    text-align: center;
    font-family: "Teko", sans-serif;
    font-weight: 500;
    font-size: 56px;
    line-height: 1;
    letter-spacing: 1px;
    text-transform: uppercase;
  }
</style>
</head>
<body>
  <main class="banner">
    <div class="banner__turf" role="img" aria-label="Pelouse de terrain de football vue de près, en tons verts"></div>

    <div class="club-mark">
      <span class="club-mark__square"></span>
      <span class="club-mark__name">FC MORLAN</span>
    </div>

    <h2 class="kicker silver">GRANDE TOMBOLA</h2>

    <h1 class="headline silver">
      <span class="headline__line headline__line--first">Fête des lanternes</span>
      <span class="headline__line headline__line--second">d'hiver</span>
    </h1>

    <a class="cta" href="#">Plus d'informations</a>

    <p class="tagline silver">Soutenez le FC Morlan et les restaurateurs locaux</p>
  </main>
</body>
</html>
```